new branding The Velvet Sip House

The Velvet Sip House is a Belgian brand of ready to serve mocktails. We're looking for a rebranding of the labels on our bottles (8 different flavours)
Our mocktails are low in sugar, 100% natural and completely alcohol-free. They are also 'ready to serve': gently shake the bottle, serve with ice cubes, finish and your mocktail is ready in no time!
Besides being the ideal aperitif, you can also serve them during brunch or dinner. Thanks to the different flavors, you can pair each mocktail with a dish.
Please visit our website to see the current look&feel: the velvetsiphouse.com - https://thevelvetsiphouse.glimmerfold.com/

Target Market(s)

people looking for a premium alcoholfree alternative - premium market

Industry/Entity Type

Mocktails (our mocktails have unique flavors, it's not the non-alcoholic version of a cocktail)

Colors

Designer to choose colors to be used in the design.

Requirements
Must have
• Our brand should be more visible, more recognizable, bolder, without losing the premium and refined character. Base colors should be white, black and silver. The brand should be put more foward. Keep number concept (every mocktail has its number) Put the ingredients/flavours/combinations a bit more forward. make the brand more confident and mature. The eight bottles should become a family. PREMIUM EXPRESSION
Nice to have
• We want to work with a white label. Ideas for the shape of the label Some ideas for the label: Play with shapes, cut outs, texture and number of labels. We like the frosted look and the combination of print & label . Working with 2 labels gives it more dynamic, not one big block Clean label. Working with a cut out shape, can be the logo or the numbers ? Working with 2 labels makes it easier to create an importance of messages. Working with an organic shape makes it unique and give a natural touch Working with a cut out can give a color pop on the white label The label can have parts coming out of the square shape
Should not have
• No crazy stuff, finishes etc should be feasible/realistic

```html
<!DOCTYPE html>
<html lang="en">
<head>
<meta charset="utf-8">
<title>The Velvet Sip House — Bottle Labels</title>
<link rel="stylesheet" href="https://fonts.googleapis.com/css2?family=Montserrat:wght@400;500;600;700;800&family=Playfair+Display:wght@700;900&display=swap">
<style>
  :root {
    --bg-top: #b8b5e6;
    --bg-bottom: #b5dbfd;
    --label-white: #f6f6f6;
    --silver: #a9a9a9;
    --silver-dark: #7c7c7c;
    --silver-light: #d9d9d9;
    --ink: #1c1c1c;
    --ink-soft: #333333;
    --basil: #9eae6c;
    --apple: #e8474a;
    --sketch: #c9c9c9;
  }
  * { margin: 0; padding: 0; box-sizing: border-box; }
  html, body { width: 1200px; height: 839px; overflow: hidden; }
  body {
    background: linear-gradient(180deg, var(--bg-top) 0%, var(--bg-bottom) 100%);
    font-family: "Montserrat", sans-serif;
    color: var(--ink);
    position: relative;
  }
  .label-set { position: absolute; top: 316px; width: 231px; height: 380px; }
  .label-set--basil { left: 268px; }
  .label-set--apple { left: 672px; }

  .hex-label { position: absolute; left: 11px; top: 0; width: 209px; height: 269px; }
  .hex-label__shape { position: absolute; inset: 0; }
  .hex-label__number {
    position: absolute; top: 24px; width: 100%; text-align: center;
    font-weight: 600; font-size: 16px; color: var(--ink-soft);
  }
  .hex-label__number b {
    font-family: "Playfair Display", serif; font-weight: 900; font-size: 30px;
    color: var(--ink); margin-left: 2px; vertical-align: -3px;
  }
  .hex-label__brand {
    position: absolute; top: 82px; width: 100%; text-align: center;
    font-weight: 600; color: var(--silver-dark); letter-spacing: 2px; line-height: 1.05;
  }
  .hex-label__brand .the { display: block; font-size: 13px; letter-spacing: 4px; }
  .hex-label__brand .name { display: block; font-size: 19px; }
  .hex-label__tagline {
    position: absolute; top: 166px; left: 12px; width: 185px; height: 26px;
    background: var(--silver); color: #f0f0f0; border-radius: 3px;
    font-size: 8.6px; font-weight: 500; letter-spacing: .2px;
    display: flex; align-items: center; justify-content: center;
  }
  .hex-label__sprig {
    position: absolute; top: 198px; left: 38px; width: 132px; height: 58px;
    background: linear-gradient(160deg, var(--sketch), #e6e6e6);
    border-radius: 40% 60% 30% 50%; opacity: .7;
  }

  .flavour-label {
    position: absolute; left: 0; top: 277px; width: 231px; height: 102px;
    background: var(--label-white);
    border-top: 2px dotted #e2e2e2; border-bottom: 2px dotted #e2e2e2;
  }
  .flavour-label__band {
    position: absolute; left: 5px; right: 5px; top: 6px; height: 54px;
    border-radius: 4px;
  }
  .label-set--basil .flavour-label__band { background: var(--basil); }
  .label-set--apple .flavour-label__band { background: var(--apple); }
  .flavour-label__name {
    position: absolute; top: 8px; width: 100%; text-align: center;
    font-size: 16.5px; font-weight: 500; letter-spacing: -.2px;
  }
  .label-set--basil .flavour-label__name { color: #151515; }
  .label-set--apple .flavour-label__name { color: #151515; font-weight: 600; }
  .flavour-label__pill {
    position: absolute; top: 32px; left: 50%; transform: translateX(-50%);
    background: #fff; border-radius: 8px; padding: 1px 11px;
    font-size: 9px; font-weight: 600; white-space: nowrap;
  }
  .flavour-label__footer {
    position: absolute; left: 8px; right: 8px; top: 64px; height: 32px;
    display: flex; align-items: center; justify-content: space-between;
  }
  .flavour-label__note {
    font-size: 8px; font-weight: 500; line-height: 1.05; text-align: center;
  }
  .flavour-label__brand {
    display: flex; align-items: center; gap: 4px;
    font-size: 8.5px; font-weight: 800; letter-spacing: 1.5px; text-align: center; line-height: 1.2;
  }
  .flavour-label__brand .dot { width: 5px; height: 5px; border-radius: 50%; background: var(--ink); }
</style>
</head>
<body>

<section class="label-set label-set--basil">
  <div class="hex-label">
    <svg class="hex-label__shape" viewBox="0 0 209 269" aria-hidden="true">
      <defs>
        <linearGradient id="silverEdge" x1="0" y1="0" x2="1" y2="1">
          <stop offset="0" stop-color="#6e6e6e"/><stop offset=".5" stop-color="#c8c8c8"/><stop offset="1" stop-color="#7d7d7d"/>
        </linearGradient>
      </defs>
      <polygon points="104.5,2 207,61 207,208 104.5,267 2,208 2,61" fill="#ffffff" stroke="url(#silverEdge)" stroke-width="4"/>
      <polygon points="104.5,9 201,64 201,205 104.5,260 8,205 8,64" fill="#f1f1f1" stroke="#555" stroke-width="1.5"/>
    </svg>
    <div class="hex-label__number">N°<b>1</b></div>
    <div class="hex-label__brand"><span class="the">THE</span><span class="name">VELVET SIP</span><span class="name">HOUSE</span></div>
    <div class="hex-label__tagline">PREMIUM NON-ALCOHOLIC DRINK</div>
    <div class="hex-label__sprig" role="img" aria-label="Fine line sketch of an olive sprig"></div>
  </div>
  <div class="flavour-label">
    <div class="flavour-label__band"></div>
    <div class="flavour-label__name">BASIL &amp; ELDERFLOWER</div>
    <div class="flavour-label__pill">FRESH FRUIIT &amp; HERBS</div>
    <div class="flavour-label__footer">
      <div class="flavour-label__note">ALCOHOL<br>FREE</div>
      <div class="flavour-label__brand"><span class="dot"></span><span>VELVET SIP<br>HOUSE</span></div>
      <div class="flavour-label__note">MADE IN<br>BELGIUM</div>
    </div>
  </div>
</section>

<section class="label-set label-set--apple">
  <div class="hex-label">
    <svg class="hex-label__shape" viewBox="0 0 209 269" aria-hidden="true">
      <polygon points="104.5,2 207,61 207,208 104.5,267 2,208 2,61" fill="#ffffff" stroke="url(#silverEdge)" stroke-width="4"/>
      <polygon points="104.5,9 201,64 201,205 104.5,260 8,205 8,64" fill="#f1f1f1" stroke="#555" stroke-width="1.5"/>
    </svg>
    <div class="hex-label__number">N°<b>7</b></div>
    <div class="hex-label__brand"><span class="the">THE</span><span class="name">VELVET SIP</span><span class="name">HOUSE</span></div>
    <div class="hex-label__tagline">PREMIUM NON-ALCOHOLIC DRINK</div>
    <div class="hex-label__sprig" role="img" aria-label="Fine line sketch of an olive sprig"></div>
  </div>
  <div class="flavour-label">
    <div class="flavour-label__band"></div>
    <div class="flavour-label__name">APPLE &amp; THYME</div>
    <div class="flavour-label__pill">FRESH FRUIIT &amp; HERBS</div>
    <div class="flavour-label__footer">
      <div class="flavour-label__note">ALCOHOL<br>FREE</div>
      <div class="flavour-label__brand"><span class="dot"></span><span>VELVET SIP<br>HOUSE</span></div>
      <div class="flavour-label__note">MADE IN<br>BELGIUM</div>
    </div>
  </div>
</section>

</body>
</html>
```